Irrigation Business needs their business cards modernised and revamped

I would like to keep my current logo, colours and revamp the format of the card.

I would like the card to be clean yet important.

Im not sure if you include texture but i would like the named logo to be indented into the card etc.

show me something alive and free something thats clinical to the point yet has a feel of achievement. i would like people to go nice card.

Target Market(s)

high end clients, corporate, sports field manger, the guys that make the decisions

Industry/Entity Type

Business

Contact Information for Business Card

nformation to be included

Dorian Hesk (Director)
0487253916
dorian@tfcraft.biz
www.taddsfieldcrafts.com

instagram logo
google logo
facebook logo

Colors

Designer to choose colors to be used in the design.

Requirements
Nice to have
• indentations a really nice feel to the card good texture

```html
<!DOCTYPE html>
<html lang="en">
<head>
<meta charset="utf-8">
<title>Tadd's Field Crafts – Business Card</title>
<link href="https://fonts.googleapis.com/css2?family=Roboto:wght@400;700&display=swap" rel="stylesheet">
<style>
  :root {
    --page-bg: #e9ecef;
    --card-white: #ffffff;
    --brand-blue: #2ea3d6;
    --brand-blue-deep: #2a8fc0;
    --ink-blue: #2c5fae;
    --ink-grey: #8a8f96;
    --rule-blue: #3a9fd8;
    --icon-grey: #9aa1a8;
  }
  * { box-sizing: border-box; margin: 0; padding: 0; }
  html, body {
    width: 1200px; height: 786px; overflow: hidden;
    background: var(--page-bg);
    font-family: "Roboto", Arial, sans-serif;
  }
  .sheet {
    width: 1200px; height: 786px;
    display: flex; align-items: center; justify-content: center; gap: 40px;
  }
  .card {
    position: relative;
    width: 540px; height: 309px;
    border-radius: 4px;
    overflow: hidden;
    box-shadow: 0 6px 18px rgba(0,0,0,0.14);
  }
  /* Front */
  .card-front { background: var(--card-white); }
  .front-brand {
    position: absolute; left: 40px; top: 104px;
    display: flex; align-items: center; gap: 12px;
  }
  .brand-dot {
    width: 46px; height: 46px; border-radius: 50%;
    background: var(--ink-blue); flex: none;
  }
  .brand-name {
    font-weight: 700; font-size: 20px; letter-spacing: 0.5px;
    color: var(--ink-blue); text-transform: uppercase; line-height: 1.1;
    width: 170px;
  }
  .social-row {
    position: absolute; left: 104px; top: 212px;
    display: flex; gap: 8px;
  }
  .social-chip {
    width: 14px; height: 14px; border-radius: 50%;
    background: var(--icon-grey);
  }
  .divider {
    position: absolute; left: 270px; top: 76px;
    width: 2px; height: 150px; background: var(--rule-blue);
  }
  .contact {
    position: absolute; left: 294px; top: 84px;
  }
  .person-name {
    font-weight: 700; font-size: 22px; color: var(--ink-blue);
  }
  .person-role {
    font-size: 15px; color: var(--ink-grey); margin-top: 2px; margin-bottom: 16px;
  }
  .contact-line {
    display: flex; align-items: center; gap: 8px;
    font-size: 13px; color: var(--ink-grey); margin-bottom: 7px;
  }
  .contact-line svg { width: 12px; height: 12px; flex: none; }
  /* Back */
  .card-back { background: var(--brand-blue); }
  .back-decor {
    position: absolute; right: -70px; bottom: -120px;
    width: 360px; height: 360px; border-radius: 50%;
    background: var(--brand-blue-deep);
  }
  .back-brand {
    position: absolute; left: 50%; top: 50%;
    transform: translate(-50%, -50%);
    display: flex; align-items: center; gap: 14px;
  }
  .back-brand .brand-dot { background: var(--card-white); width: 54px; height: 54px; }
  .back-brand .brand-name { color: var(--card-white); font-size: 24px; width: 210px; }
</style>
</head>
<body>
<main class="sheet">
  <section class="card card-front" aria-label="Business card front">
    <div class="front-brand">
      <span class="brand-dot"></span>
      <span class="brand-name">Tadd's Field Crafts</span>
    </div>
    <div class="social-row" aria-label="Social links">
      <span class="social-chip"></span>
      <span class="social-chip"></span>
      <span class="social-chip"></span>
    </div>
    <div class="divider"></div>
    <div class="contact">
      <p class="person-name">Dorian Hesk</p>
      <p class="person-role">Director</p>
      <p class="contact-line">
        <svg viewBox="0 0 12 12"><path d="M3 1 L5 3.5 L4 5 Q5.5 7.5 7 8 L8.5 7 L11 9 L9.5 11 Q4 10 1 3 Z" fill="#2ea3d6"/></svg>
        0487253916
      </p>
      <p class="contact-line">
        <svg viewBox="0 0 12 12"><rect x="1" y="2.5" width="10" height="7" fill="#2ea3d6"/><path d="M1 2.5 L6 6.5 L11 2.5" stroke="#fff" fill="none" stroke-width="1"/></svg>
        dorian@tfcraft.biz
      </p>
      <p class="contact-line">
        <svg viewBox="0 0 12 12"><circle cx="6" cy="6" r="5" fill="none" stroke="#2ea3d6" stroke-width="1.2"/><path d="M1 6 H11 M6 1 Q3 6 6 11 Q9 6 6 1" fill="none" stroke="#2ea3d6" stroke-width="1"/></svg>
        www.taddsfieldcrafts.com
      </p>
    </div>
  </section>

  <section class="card card-back" aria-label="Business card back">
    <div class="back-decor"></div>
    <div class="back-brand">
      <span class="brand-dot"></span>
      <span class="brand-name">Tadd's Field Crafts</span>
    </div>
  </section>
</main>
</body>
</html>
```